Brackenly.com Postcard

We want to create a postcard, which is going to be mailed out to 6k managers at Hospitals throughout the USA.

I attached a rough draft of what I want the postcard to look like, but want it to look much better. The postcard size is 5.47" * 4.21"

```html
<!DOCTYPE html>
<html lang="en">
<head>
<meta charset="utf-8">
<title>Brackenly Medical Postcard</title>
<link href="https://fonts.googleapis.com/css2?family=Libre+Baskerville:wght@400;700&display=swap" rel="stylesheet">
<style>
:root{
  --bg:#e6e6ea;
  --card:#ffffff;
  --purple:#3a3a8e;
  --purple-deep:#2b2a72;
  --lavender:#8f92d2;
  --mist:#d9dae6;
  --ink:#1d1d24;
  --text:#3c3c46;
  --rule:#8a8a94;
}
*{margin:0;padding:0;box-sizing:border-box}
html,body{width:766px;height:1200px;overflow:hidden;background:var(--bg)}
body{font-family:"Libre Baskerville",Georgia,serif;color:var(--text);position:relative}
.card{position:absolute;left:51px;width:664px;height:511px;background:var(--card);overflow:hidden;box-shadow:0 4px 14px rgba(0,0,0,.18)}
.card--front{top:52px}
.card--back{top:628px;height:520px}
.swoosh{position:absolute;inset:0;width:100%;height:100%}
.hero-photo{position:absolute;left:170px;top:40px;width:380px;height:250px;border-radius:48% 48% 50% 50%/55% 55% 45% 45%;background:radial-gradient(ellipse at 40% 35%,#e0454a 0%,#b3121c 55%,#7d0a12 100%);box-shadow:0 18px 22px rgba(0,0,0,.18)}
.brand{position:absolute;display:flex;align-items:center;gap:10px;color:var(--purple-deep);font-variant:small-caps;letter-spacing:.5px}
.brand__dot{display:block;border-radius:50%;background:var(--purple-deep)}
.card--front .brand{left:50px;top:432px;font-size:38px}
.card--front .brand__dot{width:34px;height:34px}
.card--back .brand{left:28px;top:30px;font-size:22px}
.card--back .brand__dot{width:22px;height:22px}
.back-copy{position:absolute;left:0;top:82px;width:322px;text-align:center}
.tagline-band{background:var(--mist);padding:8px 0 10px}
.tagline{color:var(--purple);font-size:27px;font-weight:700;text-decoration:underline;text-underline-offset:4px}
.headline{margin:20px 22px 0;font-size:22px;line-height:1.3;font-weight:700;color:var(--ink)}
.body-text{margin:16px 30px 0;font-size:13.5px;line-height:1.55;color:var(--text)}
.cta{margin:18px 16px 0;font-size:15px;line-height:1.35;font-weight:700;color:var(--purple);text-transform:uppercase}
.contact{position:absolute;left:26px;top:452px;width:290px;display:grid;grid-template-columns:auto auto;justify-content:start;gap:0 22px;font-size:10.5px;line-height:1.45;color:var(--ink)}
.contact__item{display:flex;gap:6px;align-items:flex-start}
.contact__item svg{flex:none;margin-top:2px}
.stamp{position:absolute;left:548px;top:110px;width:52px;height:60px;border:1.5px solid var(--rule)}
.address-line{position:absolute;left:468px;width:170px;height:0;border-top:1.5px solid var(--rule)}
</style>
</head>
<body>

<section class="card card--front">
  <svg class="swoosh" viewBox="0 0 664 511" aria-hidden="true">
    <defs>
      <linearGradient id="floor" x1="0" y1="0" x2="0" y2="1">
        <stop offset="0" stop-color="#ffffff"/>
        <stop offset="1" stop-color="#dcdce4"/>
      </linearGradient>
    </defs>
    <rect x="0" y="330" width="664" height="181" fill="url(#floor)"/>
    <path d="M0 300 C180 250 420 400 664 210 L664 270 C430 450 190 330 0 380 Z" fill="var(--lavender)"/>
    <path d="M0 380 C190 330 430 450 664 270 L664 318 C440 480 200 380 0 430 Z" fill="var(--purple)"/>
    <path d="M0 430 C200 380 440 480 664 318 L664 342 C450 500 210 410 0 455 Z" fill="#ffffff"/>
  </svg>
  <div class="hero-photo" role="img" aria-label="Red glossy heart with an IV drip line and bag attached"></div>
  <div class="brand"><span class="brand__dot"></span>Brackenly Medical</div>
</section>

<section class="card card--back">
  <svg class="swoosh" viewBox="0 0 664 520" aria-hidden="true">
    <path d="M330 0 C305 160 355 360 340 520 L390 520 C445 360 385 150 420 0 Z" fill="var(--lavender)"/>
    <path d="M420 0 C385 150 445 360 390 520 L425 520 C480 360 418 150 452 0 Z" fill="var(--purple)"/>
    <path d="M452 0 C418 150 480 360 425 520 L437 520 C492 360 430 150 466 0 Z" fill="var(--mist)"/>
  </svg>

  <div class="brand"><span class="brand__dot"></span>Brackenly Medical</div>

  <div class="back-copy">
    <div class="tagline-band"><h2 class="tagline">We Buy IV Pumps</h2></div>
    <h1 class="headline">Looking To Sell Your Infusion IV Pumps?</h1>
    <p class="body-text">Brackenly Medical will purchase your infusion iv pumps. We will buy all of your quality iv pumps. We offer competitive pricing and will purchase from companies and individuals.</p>
    <p class="cta">Sell infusion pumps to<br>Brackenly Medical today!</p>
  </div>

  <div class="contact">
    <div class="contact__item">
      <svg width="9" height="12" viewBox="0 0 9 12"><path d="M4.5 0A4.5 4.5 0 0 0 0 4.5C0 8 4.5 12 4.5 12S9 8 9 4.5A4.5 4.5 0 0 0 4.5 0Zm0 6.2a1.7 1.7 0 1 1 0-3.4 1.7 1.7 0 0 1 0 3.4Z" fill="var(--purple)"/></svg>
      <span>Brackenly Medical<br>PO Box 3170<br>Fernwood, NC 27001</span>
    </div>
    <div class="contact__item">
      <svg width="11" height="11" viewBox="0 0 11 11"><path d="M2.3 0.5 4 2.6 3 4a6.5 6.5 0 0 0 4 4l1.4-1 2.1 1.7-1 1.8C5 10.5.5 6 .5 1.5Z" fill="var(--purple)"/></svg>
      <span>555-014-2290<br>sales@brackenly.com<br>Brackenly.com</span>
    </div>
  </div>

  <div class="stamp"></div>
  <div class="address-line" style="top:300px"></div>
  <div class="address-line" style="top:330px"></div>
  <div class="address-line" style="top:360px"></div>
</section>

</body>
</html>
```